Facebook ads needed for Pharmacy Continuing Education

I need 5 different Facebook ads in 3 sizes:

1080X1080, ratio 1:1
1080x1920
1200x628

I need the created ads in .psd format. Please ensure that all fonts used in the PSD file are standard system fonts or commonly available fonts in Adobe Photoshop (e.g., from the Adobe Fonts library). Do not use paid or third-party fonts that are not included with Photoshop by default.

Please check out the MedLoop.com homepage to get an idea of the look and feel of the images we want. I have also uploaded some past ads we like
and our logo.

Text:

Free California Cultural Competency CE for Pharmacy Techs

NBTQ Approved
Easy-To-Use
DLQ Tracker Submission

Button: Get Your Free Course

```html
<!DOCTYPE html>
<html lang="en">
<head>
<meta charset="utf-8">
<title>MedLoop – Free Cultural Competency CE – Ad Sizes</title>
<link rel="stylesheet" href="https://fonts.googleapis.com/css2?family=Anton&family=Archivo+Black&family=Arimo:wght@400;700&display=swap">
<style>
  :root{
    --navy:#124a6e;
    --teal:#2f6f62;
    --green:#6aa244;
    --blue:#2a78b0;
    --orange:#e49234;
    --logo-blue:#1f4e86;
    --ink:#111;
    --white:#fff;
    --art-grey:#dfe5ea;
    --dots:#cfe3c2;
  }
  *{box-sizing:border-box;margin:0;padding:0}
  html,body{width:1200px;height:1200px;overflow:hidden;background:var(--white)}
  body{position:relative;font-family:"Arimo",Arial,sans-serif}

  .size-label{position:absolute;transform:translateX(-50%);font-family:"Anton",Impact,sans-serif;color:var(--ink);letter-spacing:.32em;white-space:nowrap;line-height:1}
  .size-label.lg{font-size:34px}
  .size-label.md{font-size:25px}

  .ad{position:absolute;overflow:hidden;background:
      radial-gradient(ellipse 45% 18% at 50% 100%, rgba(106,162,68,.85), rgba(106,162,68,0) 100%),
      linear-gradient(90deg,var(--navy) 0%,var(--teal) 30%,var(--green) 50%,var(--teal) 70%,var(--navy) 100%);
      box-shadow:0 22px 30px -12px rgba(0,0,0,.35)}
  .ad-hero{position:absolute;left:0;top:0;width:100%;background:var(--white)}
  .brand-stripe{position:absolute;left:0;width:100%;display:flex}
  .brand-stripe span{flex:1}
  .brand-stripe span:nth-child(1){background:var(--navy)}
  .brand-stripe span:nth-child(2){background:var(--blue)}
  .brand-stripe span:nth-child(3){background:var(--green)}
  .brand-stripe span:nth-child(4){background:var(--orange)}

  .brand-name{position:absolute;font-family:"Arimo",Arial,sans-serif;font-weight:700;color:var(--logo-blue);line-height:1;white-space:nowrap}
  .team-art{position:absolute;border-radius:40% 40% 0 0;background:linear-gradient(180deg,var(--art-grey),#eef1f4)}
  .dot-field{position:absolute;background:var(--dots);opacity:.6}
  .dot-field.light{background:rgba(255,255,255,.35)}

  .headline-free{position:absolute;font-family:"Archivo Black","Arial Black",sans-serif;color:var(--white);line-height:1;letter-spacing:-.03em;white-space:nowrap}
  .course-title{position:absolute;color:var(--white);font-weight:400}
  .features{position:absolute;display:flex;color:var(--white);white-space:nowrap}
  .feature{display:flex;align-items:center}
  .tick{flex:none}
  .cta{position:absolute;background:var(--orange);color:var(--white);display:flex;align-items:center;white-space:nowrap;line-height:1.05}
  .cta b{color:var(--ink);font-weight:700}

  /* square */
  .ad-square{left:66px;top:141px;width:586px;height:586px}
  .ad-square .ad-hero{height:166px}
  .ad-square .brand-stripe{top:166px;height:5px}
  .ad-square .headline-free{left:0;width:100%;text-align:center;top:196px;font-size:172px;transform:scaleX(.97)}
  .ad-square .course-title{left:0;width:100%;text-align:center;top:344px;font-size:35px;line-height:36px}
  .ad-square .features{left:0;width:100%;justify-content:center;top:432px;font-size:17.5px;gap:12px}
  .ad-square .feature{gap:6px}
  .ad-square .cta{left:80px;top:485px;width:426px;height:65px;border-radius:33px;justify-content:center;font-size:32px}

  /* portrait */
  .ad-portrait{left:711px;top:122px;width:368px;height:653px}
  .ad-portrait .ad-hero{height:102px}
  .ad-portrait .brand-stripe{top:102px;height:4px}
  .ad-portrait .headline-free{left:0;width:100%;text-align:center;top:136px;font-size:112px;transform:scaleX(.93)}
  .ad-portrait .course-title{left:0;width:100%;text-align:center;top:247px;font-size:30px;line-height:38.5px}
  .ad-portrait .features{left:56px;top:420px;flex-direction:column;gap:17px;font-size:20px}
  .ad-portrait .feature{gap:6px}
  .ad-portrait .cta{left:53px;top:568px;width:269px;height:41px;border-radius:21px;justify-content:center;font-size:22px}

  /* wide */
  .ad-wide .ad-hero{height:157px}
  .ad-wide .brand-stripe{height:4px}
  .ad-wide .headline-free{font-size:84px;left:28px;transform:scaleX(.85);transform-origin:left top}
  .ad-wide .course-title{left:236px;font-size:17px;line-height:22px}
  .ad-wide .features{left:34px;font-size:14px;gap:9px}
  .ad-wide .feature{gap:4px}
  .ad-wide .cta{right:0;width:140px;height:55px;border-radius:28px 0 0 28px;padding-left:17px;font-size:17px}

  .ad-link{left:38px;top:837px;width:551px;height:290px}
  .ad-link .brand-stripe{top:155px}
  .ad-link .headline-free{top:162px}
  .ad-link .course-title{top:175px}
  .ad-link .features{top:256px}
  .ad-link .cta{top:182px}

  .ad-banner{left:619px;top:828px;width:551px;height:308px}
  .ad-banner .ad-hero{height:156px}
  .ad-banner .brand-stripe{top:154px}
  .ad-banner .headline-free{top:171px}
  .ad-banner .course-title{top:182px}
  .ad-banner .features{top:264px}
  .ad-banner .cta{top:180px}
</style>
</head>
<body>

<svg width="0" height="0" style="position:absolute" aria-hidden="true">
  <symbol id="tick-box" viewBox="0 0 20 20">
    <rect x="1.5" y="3.5" width="15" height="15" fill="none" stroke="#e49234" stroke-width="2"/>
    <path d="M4.5 10.5 L8.5 15 L18 1.5" fill="none" stroke="#e49234" stroke-width="2.4" stroke-linecap="round" stroke-linejoin="round"/>
  </symbol>
</svg>

<div class="size-label lg" style="left:342px;top:62px">1080X1080</div>
<div class="size-label md" style="left:897px;top:45px">1080X1920 (PORTRAIT)</div>
<div class="size-label lg" style="left:342px;top:785px">1200X628</div>
<div class="size-label md" style="left:897px;top:804px">1080X1920 (LANDSCAPE)</div>

<!-- Square ad -->
<section class="ad ad-square">
  <div class="ad-hero">
    <div class="dot-field" style="left:29px;top:23px;width:30px;height:28px" role="img" aria-label="Dot grid accent"></div>
    <div class="brand-name" style="left:37px;top:85px;font-size:44px">MedLoop</div>
    <div class="team-art" style="left:268px;top:9px;width:310px;height:157px" role="img" aria-label="Illustration of four pharmacy professionals in white coats"></div>
  </div>
  <div class="brand-stripe"><span></span><span></span><span></span><span></span></div>
  <div class="headline-free">FREE</div>
  <div class="course-title">California Cultural Competency<br>CE for Pharmacy Techs</div>
  <div class="features">
    <span class="feature"><svg class="tick" width="20" height="20"><use href="#tick-box"/></svg>NBTQ Approved</span>
    <span class="feature"><svg class="tick" width="20" height="20"><use href="#tick-box"/></svg>Easy-To-Use</span>
    <span class="feature"><svg class="tick" width="20" height="20"><use href="#tick-box"/></svg>DLQ Tracker Submission</span>
  </div>
  <div class="cta">Get Your&nbsp;<b>Free</b>&nbsp;Course</div>
  <div class="dot-field light" style="left:528px;top:543px;width:30px;height:28px" role="img" aria-label="Dot grid accent"></div>
</section>

<!-- Portrait ad -->
<section class="ad ad-portrait">
  <div class="ad-hero">
    <div class="dot-field" style="left:19px;top:9px;width:41px;height:18px" role="img" aria-label="Dot grid accent"></div>
    <div class="brand-name" style="left:23px;top:45px;font-size:30px">MedLoop</div>
    <div class="team-art" style="left:170px;top:2px;width:198px;height:100px" role="img" aria-label="Illustration of four pharmacy professionals in white coats"></div>
  </div>
  <div class="brand-stripe"><span></span><span></span><span></span><span></span></div>
  <div class="headline-free">FREE</div>
  <div class="course-title">California Cultural<br>Competency<br>CE for Pharmacy<br>Techs</div>
  <div class="features">
    <span class="feature"><svg class="tick" width="24" height="24"><use href="#tick-box"/></svg>NBTQ Approved</span>
    <span class="feature"><svg class="tick" width="24" height="24"><use href="#tick-box"/></svg>Easy-To-Use</span>
    <span class="feature"><svg class="tick" width="24" height="24"><use href="#tick-box"/></svg>DLQ Tracker Submission</span>
  </div>
  <div class="cta">Get Your&nbsp;<b>Free</b>&nbsp;Course</div>
  <div class="dot-field light" style="left:303px;top:617px;width:40px;height:18px" role="img" aria-label="Dot grid accent"></div>
</section>

<!-- 1200x628 ad -->
<section class="ad ad-wide ad-link">
  <div class="ad-hero">
    <div class="dot-field" style="left:29px;top:19px;width:55px;height:24px" role="img" aria-label="Dot grid accent"></div>
    <div class="brand-name" style="left:35px;top:90px;font-size:34px">MedLoop</div>
    <div class="team-art" style="left:253px;top:12px;width:298px;height:145px" role="img" aria-label="Illustration of four pharmacy professionals in white coats"></div>
  </div>
  <div class="brand-stripe"><span></span><span></span><span></span><span></span></div>
  <div class="headline-free">FREE</div>
  <div class="course-title">California Cultural<br>Competency CE for<br>Pharmacy Techs</div>
  <div class="cta"><span>Get Your<br><b>Free</b> Course</span></div>
  <div class="features">
    <span class="feature"><svg class="tick" width="17" height="17"><use href="#tick-box"/></svg>NBTQ Approved</span>
    <span class="feature"><svg class="tick" width="17" height="17"><use href="#tick-box"/></svg>Easy-To-Use</span>
    <span class="feature"><svg class="tick" width="17" height="17"><use href="#tick-box"/></svg>DLQ Tracker Submission</span>
  </div>
  <div class="dot-field light" style="left:475px;top:256px;width:53px;height:24px" role="img" aria-label="Dot grid accent"></div>
</section>

<!-- Landscape ad -->
<section class="ad ad-wide ad-banner">
  <div class="ad-hero">
    <div class="dot-field" style="left:29px;top:17px;width:55px;height:24px" role="img" aria-label="Dot grid accent"></div>
    <div class="brand-name" style="left:36px;top:84px;font-size:36px">MedLoop</div>
    <div class="team-art" style="left:253px;top:5px;width:298px;height:151px" role="img" aria-label="Illustration of four pharmacy professionals in white coats"></div>
  </div>
  <div class="brand-stripe"><span></span><span></span><span></span><span></span></div>
  <div class="headline-free">FREE</div>
  <div class="course-title">California Cultural<br>Competency CE for<br>Pharmacy Techs</div>
  <div class="cta"><span>Get Your<br><b>Free</b> Course</span></div>
  <div class="features">
    <span class="feature"><svg class="tick" width="17" height="17"><use href="#tick-box"/></svg>NBTQ Approved</span>
    <span class="feature"><svg class="tick" width="17" height="17"><use href="#tick-box"/></svg>Easy-To-Use</span>
    <span class="feature"><svg class="tick" width="17" height="17"><use href="#tick-box"/></svg>DLQ Tracker Submission</span>
  </div>
  <div class="dot-field light" style="left:479px;top:263px;width:53px;height:24px" role="img" aria-label="Dot grid accent"></div>
</section>

</body>
</html>
```